Plumwave business card

We need a modern business card - With our 4 colors - See web: www.plumwave.dk

I have attached logo and som old business Cards we have - Lets Make the new ones shine...:-) -

Industry/Entity Type

Business

Requirements
Must have
• the logo with plumwave only,

```html
<!DOCTYPE html>
<html lang="da">
<head>
<meta charset="utf-8">
<title>Plumwave – visitkort</title>
<link rel="stylesheet" href="https://fonts.googleapis.com/css2?family=Arimo:ital,wght@0,400;0,700;1,700&display=swap">
<style>
  :root {
    --page: #e7e6e3;
    --card: #f4f5f4;
    --card-edge: #d6d8d6;
    --green: #5aa02c;
    --plum: #8b2a6e;
    --orange: #c4741c;
    --ink: #3a3a3a;
    --ink-soft: #4a4a4a;
    --band-text: #f2e9f0;
  }
  * { margin: 0; padding: 0; box-sizing: border-box; }
  html, body { width: 1200px; height: 969px; overflow: hidden; }
  body {
    background: var(--page);
    font-family: "Arimo", Arial, sans-serif;
    position: relative;
  }
  .card {
    position: absolute;
    left: 100px; top: 202px;
    width: 1000px; height: 564px;
    background: var(--card);
    border: 1px solid var(--card-edge);
    box-shadow: 0 10px 30px rgba(0,0,0,0.12);
  }
  .person { position: absolute; left: 55px; top: 100px; }
  .person-name { font-size: 32px; font-weight: 700; color: var(--green); }
  .person-title { font-size: 24px; color: var(--ink); margin-top: 6px; }
  .address {
    position: absolute; left: 57px; top: 218px;
    font-size: 25px; line-height: 37px; color: var(--ink-soft);
  }
  .contacts {
    position: absolute; left: 55px; top: 345px;
    list-style: none; font-size: 25px; color: var(--ink-soft);
  }
  .contacts li { display: flex; align-items: center; height: 38px; }
  .contacts svg { width: 26px; height: 22px; margin-right: 20px; fill: var(--green); }
  .brand {
    position: absolute; left: 585px; top: 190px; width: 328px;
    text-align: center;
  }
  .brand-row { display: flex; align-items: center; justify-content: center; gap: 14px; }
  .brand-dot { width: 30px; height: 30px; border-radius: 50%; background: var(--green); }
  .brand-name { font-size: 30px; color: var(--ink); letter-spacing: 1px; }
  .brand-rule { height: 3px; background: var(--green); margin-top: 16px; }
  .brand-tagline { font-size: 18px; font-weight: 700; color: var(--ink); margin-top: 22px; }
  .web-band {
    position: absolute; left: 0; right: 0; top: 500px; height: 44px;
    background: linear-gradient(90deg, var(--plum) 0%, #9a3a78 45%, #5a8a2a 80%, var(--orange) 100%);
    display: flex; align-items: center; padding-left: 55px;
  }
  .web-url { font-size: 23px; font-weight: 700; font-style: italic; color: var(--band-text); letter-spacing: 1px; }
</style>
</head>
<body>
  <article class="card">
    <div class="person">
      <div class="person-name">Maren Lindholt</div>
      <div class="person-title">Salgsdirektør</div>
    </div>
    <div class="address">
      Lærkevej 14<br>
      5000 Odense C<br>
      Tlf. +45 31 20 40 60
    </div>
    <ul class="contacts">
      <li><svg viewBox="0 0 26 22"><path d="M2 8c0-4 5-6 11-6s11 2 11 6v2h-6V7H8v3H2z M6 12h14l3 8H3z"/></svg>+45 31 20 40 60</li>
      <li><svg viewBox="0 0 26 22"><path d="M2 8c0-4 5-6 11-6s11 2 11 6v2h-6V7H8v3H2z M6 12h14l3 8H3z"/></svg>+45 52 70 80 90</li>
      <li><svg viewBox="0 0 26 22"><path d="M2 4h22v14H2z" /><path d="M2 4l11 8 11-8" fill="none" stroke="#f4f5f4" stroke-width="2"/></svg>ml@plumwave.dk</li>
    </ul>
    <div class="brand">
      <div class="brand-row">
        <span class="brand-dot"></span>
        <span class="brand-name">plumwave</span>
      </div>
      <div class="brand-rule"></div>
      <div class="brand-tagline">lyd og billede</div>
    </div>
    <div class="web-band"><span class="web-url">www.plumwave.dk</span></div>
  </article>
</body>
</html>
```